Quillbrook Builders Business Cards

I want to use the logo and make an unique business card that shows the textured Logo with brick and builings. I want to be able to stand out when I pass out business cards.

```html
<!DOCTYPE html>
<html lang="en">
<head>
<meta charset="utf-8">
<title>Quillbrook Builders Business Cards</title>
<link rel="stylesheet" href="https://fonts.googleapis.com/css2?family=Montserrat:wght@500;700&family=Oswald:wght@500;600&display=swap">
<style>
  :root {
    --stage: #2b2b2b;
    --card-black: #050505;
    --brick: #8d3b24;
    --brick-dark: #6f2c1a;
    --accent: #ef5a2a;
    --white: #ffffff;
    --soft-white: #f1f1f1;
  }
  * { box-sizing: border-box; margin: 0; padding: 0; }
  html, body { width: 1200px; height: 800px; overflow: hidden; }
  body {
    background: var(--stage);
    font-family: "Montserrat", Arial, sans-serif;
    position: relative;
  }
  .card {
    position: absolute;
    top: 245px;
    width: 540px;
    height: 309px;
    border-radius: 18px;
    overflow: hidden;
  }
  .card-front { left: 40px; background: var(--card-black); }
  .card-back { left: 620px; background: linear-gradient(160deg, var(--brick), var(--brick-dark)); }

  .brand {
    display: flex;
    align-items: center;
    gap: 10px;
    font-family: "Oswald", Arial, sans-serif;
    font-weight: 600;
    text-transform: uppercase;
    letter-spacing: 1px;
  }
  .brand-square { width: 14px; height: 14px; background: currentColor; flex: none; }

  .card-front .brand {
    position: absolute;
    left: 34px; top: 108px;
    width: 200px;
    font-size: 27px;
    line-height: 1.05;
    color: var(--accent);
  }
  .divider {
    position: absolute;
    left: 252px; top: 30px;
    width: 2px; height: 190px;
    background: linear-gradient(to bottom, transparent, var(--accent), transparent);
  }
  .contact-block { position: absolute; left: 276px; top: 34px; color: var(--white); }
  .person-name { color: var(--accent); font-weight: 700; font-size: 26px; letter-spacing: .5px; }
  .person-role { font-size: 15px; font-weight: 500; margin: 4px 0 14px; }
  .contact-list { list-style: none; }
  .contact-list li { display: flex; align-items: center; gap: 12px; font-size: 14px; margin-bottom: 7px; }
  .contact-list svg { width: 15px; height: 15px; fill: var(--accent); flex: none; }

  .services {
    position: absolute;
    left: 0; right: 0;
    text-align: center;
    font-family: "Oswald", Arial, sans-serif;
    font-weight: 500;
    color: var(--white);
    font-size: 22px;
  }
  .card-front .services { bottom: 26px; }
  .services .dot { color: var(--accent); }

  .card-back .brand {
    position: absolute;
    left: 0; right: 0; top: 110px;
    justify-content: center;
    font-size: 38px;
    color: var(--soft-white);
  }
  .card-back .services { bottom: 40px; font-size: 21px; }
</style>
</head>
<body>
  <section class="card card-front">
    <div class="brand"><span class="brand-square"></span><span>Quillbrook Builders</span></div>
    <div class="divider"></div>
    <div class="contact-block">
      <p class="person-name">SELIN TARHAN</p>
      <p class="person-role">Founder &amp; CEO</p>
      <ul class="contact-list">
        <li><svg viewBox="0 0 24 24"><path d="M6.6 10.8a15 15 0 0 0 6.6 6.6l2.2-2.2a1 1 0 0 1 1-.25 11.4 11.4 0 0 0 3.6.6 1 1 0 0 1 1 1V20a1 1 0 0 1-1 1A17 17 0 0 1 3 4a1 1 0 0 1 1-1h3.5a1 1 0 0 1 1 1c0 1.25.2 2.45.6 3.6a1 1 0 0 1-.25 1z"/></svg>012-555-014-260</li>
        <li><svg viewBox="0 0 24 24"><path d="M3 9c0-2 4-4 9-4s9 2 9 4v2h-5V9H8v2H3zM6 13h12l2 7H4z"/></svg>044-555-019-482</li>
        <li><svg viewBox="0 0 24 24"><path d="M2 12 22 3l-6 18-4-7z"/></svg>info@quillbrook.com</li>
        <li><svg viewBox="0 0 24 24"><path d="M12 2a10 10 0 1 0 0 20 10 10 0 0 0 0-20zm6.9 9h-3a15 15 0 0 0-1.3-5.6A8 8 0 0 1 18.9 11zM12 4c.9 1.2 1.7 3.5 1.9 7h-3.8c.2-3.5 1-5.8 1.9-7zM9.4 5.4A15 15 0 0 0 8.1 11h-3a8 8 0 0 1 4.3-5.6zM5.1 13h3a15 15 0 0 0 1.3 5.6A8 8 0 0 1 5.1 13zM12 20c-.9-1.2-1.7-3.5-1.9-7h3.8c-.2 3.5-1 5.8-1.9 7zm2.6-1.4a15 15 0 0 0 1.3-5.6h3a8 8 0 0 1-4.3 5.6z"/></svg>www.quillbrook.com</li>
      </ul>
    </div>
    <p class="services">Patios <span class="dot">•</span> Sidewalks <span class="dot">•</span> Retaining Walls <span class="dot">•</span> Foundations</p>
  </section>

  <section class="card card-back">
    <div class="brand"><span class="brand-square"></span><span>Quillbrook Builders</span></div>
    <p class="services">Patios - Sidewalks - Retaining Walls - Foundations</p>
  </section>
</body>
</html>
```